PowerPoint Template - Korvel Mint

You find in the attached file a short description of our firm, logo, mission, vision and values. We made an empty template in order to let you free to imagine. We-have high expectations on ideas "out of the box" to merge our job (consulting firm) with Zen concept. We really Would like "Zen" look and feel, to show our difference. And we want to avoid "standard consulting" (smart guys with ties, shaking hand with Brimlo smilies ...) Thank you

Target Market(s)

organization (Rather big ones)

Industry/Entity Type

Consulting

Number of Pages Required

3 page

Font styles to use
Sans Serif

Requirements
Must have
• - Some nice pictures - Be really "Zen" (quiet, smart, luxury, people centric)
Should not have
• really looks like "standard consulting" (smart guys with ties, shaking hand with Brimlo smilies ...)

```html
<!DOCTYPE html>
<html lang="en">
<head>
<meta charset="utf-8">
<title>Korvel Mint — Presentation Template</title>
<link rel="stylesheet" href="https://fonts.googleapis.com/css2?family=Raleway:wght@500;600;700&family=Open+Sans:wght@400;600;700&family=Fira+Sans:wght@500;600&display=swap">
<style>
  :root {
    --backdrop: #d9d9d9;
    --backdrop-light: #e6e6e6;
    --green: #a3d3a9;
    --green-deep: #8cc596;
    --orange: #f07c3c;
    --slate: #8e8f91;
    --ink: #6f6f6f;
    --ink-soft: #9a9a9a;
    --white: #ffffff;
    --paper: #f4f2ee;
  }
  * { box-sizing: border-box; margin: 0; padding: 0; }
  html, body { width: 1200px; height: 1000px; overflow: hidden; }
  body {
    background: radial-gradient(ellipse at 50% 40%, var(--backdrop-light), var(--backdrop) 75%);
    font-family: "Open Sans", sans-serif;
    color: var(--ink);
    position: relative;
  }
  .slide {
    position: absolute;
    width: 368px;
    height: 206px;
    background: var(--white);
    overflow: hidden;
    box-shadow: 0 1px 3px rgba(0,0,0,0.08);
  }
  .col-left { left: 217px; }
  .col-right { left: 615px; }
  .row-1 { top: 42px; }
  .row-2 { top: 279px; }
  .row-3 { top: 516px; }
  .row-4 { top: 752px; }

  .photo { position: absolute; }
  .abs { position: absolute; }

  .brand-mark {
    position: absolute;
    top: 9px; right: 9px;
    font-family: "Raleway", sans-serif;
    font-weight: 700;
    font-size: 6px;
    color: var(--orange);
    display: flex; align-items: center; gap: 2px;
    white-space: nowrap;
  }
  .brand-mark .dot { width: 6px; height: 6px; border-radius: 50%; border: 1px solid var(--orange); }

  .title {
    font-family: "Raleway", sans-serif;
    font-weight: 700;
    letter-spacing: -0.2px;
    text-transform: uppercase;
  }

  /* Slide 1 — cover */
  .cover .photo { inset: 0; background: linear-gradient(180deg, #f5f3ef 0%, #eeebe6 60%, #f2efea 100%); }
  .cover .band { left: 117px; top: 0; width: 134px; height: 206px; background: var(--green); opacity: 0.75; }
  .cover .notch { left: 171px; top: 0; }
  .cover .name-plate {
    left: 103px; top: 51px; width: 163px; height: 100px;
    background: var(--white);
    border: 6px solid var(--green);
    display: flex; flex-direction: column; align-items: center; justify-content: center; gap: 8px;
  }
  .cover .name-plate .ring { width: 34px; height: 34px; border-radius: 50%; border: 3px solid var(--orange); }
  .cover .name-plate .name {
    font-family: "Raleway", sans-serif; font-weight: 600; font-size: 11px;
    letter-spacing: 3px; color: var(--orange); text-transform: uppercase;
  }

  /* Slide 2 — activity intro */
  .intro .photo { left: 10px; top: 12px; width: 222px; height: 188px; background: linear-gradient(160deg, #e3f1f5 0%, #cfe4ea 55%, #b8ccd2 100%); }
  .intro .title { left: 15px; top: 24px; font-size: 16px; color: var(--ink); }
  .intro .pitch {
    left: 10px; top: 114px; width: 212px; height: 86px;
    background: var(--green);
    padding: 20px 8px 0 12px;
    font-family: "Fira Sans", sans-serif; font-weight: 600; font-size: 12.6px; line-height: 1.25;
    color: var(--white);
  }
  .intro .pitch em { font-style: normal; color: var(--orange); }
  .intro .convictions { left: 225px; top: 25px; width: 130px; height: 143px; background: var(--slate); padding: 14px 8px 0 9px; }
  .intro .convictions h3 { font-family: "Fira Sans", sans-serif; font-weight: 600; font-size: 12px; color: var(--green); margin-bottom: 8px; }
  .intro .convictions p { font-size: 5.6px; line-height: 1.55; color: var(--white); }

  /* Slide 3 — differences */
  .differences .panel { left: 0; top: 0; }
  .differences .title { left: 15px; top: 24px; font-size: 16px; color: var(--white); }
  .differences h3 { left: 42px; top: 66px; font-family: "Fira Sans", sans-serif; font-weight: 600; font-size: 16px; color: var(--ink); }
  .differences .points { left: 16px; top: 96px; width: 200px; list-style: none; }
  .differences .points li { display: flex; gap: 10px; font-size: 6px; line-height: 1.5; color: var(--white); margin-bottom: 13px; }
  .differences .points svg { flex: none; margin-top: 1px; }
  .differences .photo { left: 239px; top: 40px; width: 118px; height: 78px; background: linear-gradient(120deg, #f1f1f1 0%, #dcdcdc 60%, #b58a75 100%); }
  .differences .mission { left: 239px; top: 126px; width: 118px; }
  .differences .mission h4 { font-family: "Fira Sans", sans-serif; font-weight: 500; font-size: 13px; color: var(--ink); }
  .differences .mission p { font-size: 10px; line-height: 1.25; color: var(--ink); }

  /* Slide 4 — name explanation */
  .naming .title { left: 15px; top: 23px; font-size: 16px; color: var(--green-deep); }
  .naming .photo { left: 0; top: 110px; width: 368px; height: 96px; background: linear-gradient(180deg, #e7e6e2 0%, #d9d3ca 55%, #b88e67 100%); }
  .naming .card-outline {
    left: 52px; top: 63px; width: 123px; height: 120px;
    border: 6px solid var(--green); background: var(--white); padding: 10px 0 0 10px;
  }
  .naming .card-fill { left: 208px; top: 68px; width: 114px; height: 112px; background: var(--green); padding: 10px 0 0 7px; }
  .naming h4 { font-family: "Fira Sans", sans-serif; font-weight: 600; font-size: 16px; color: var(--orange); margin-bottom: 6px; }
  .naming ul { list-style: none; font-family: "Fira Sans", sans-serif; font-weight: 500; font-size: 8.4px; line-height: 1.3; }
  .naming .card-outline ul { color: var(--green-deep); }
  .naming .card-fill ul { color: var(--white); }

  /* Slide 5 — paradoxes */
  .paradoxes .photo { left: 0; top: 0; width: 184px; height: 206px; background: linear-gradient(180deg, #f7f7f7 0%, #ececec 70%, #f3f3f3 100%); }
  .paradoxes .shade { left: 184px; top: 0; width: 184px; height: 206px; background: var(--slate); }
  .paradoxes .title { left: 0; width: 368px; top: 22px; text-align: center; font-size: 17px; color: #6a6a6a; }
  .paradoxes .icons { left: 0; top: 0; }
  .paradoxes .label { position: absolute; font-size: 6.2px; color: var(--ink); text-align: center; width: 80px; line-height: 1.2; white-space: nowrap; }
  .paradoxes .label.on-shade { color: var(--white); }
  .paradoxes .label.wrap { white-space: normal; }

  /* Slide 6 — mission */
  .mission-slide .photo { left: 140px; top: 0; width: 228px; height: 206px; background: linear-gradient(180deg, #9b9da1 0%, #b6b7b9 45%, #c89d6c 65%, #b98c5c 100%); }
  .mission-slide .title { left: 34px; top: 23px; font-size: 16px; color: var(--orange); }
  .mission-slide .rule { left: 54px; top: 60px; width: 32px; height: 1.5px; background: var(--green); }
  .mission-slide p { left: 10px; top: 76px; width: 120px; text-align: center; font-size: 8.4px; line-height: 1.25; color: var(--ink); }

  /* Slide 7 — vision */
  .vision .photo { left: 0; top: 0; width: 186px; height: 206px; background: linear-gradient(90deg, #e4e2de 0%, #ebe8e2 40%, #e9dcc4 70%, #d9c6a4 100%); }
  .vision .title { left: 186px; width: 182px; top: 23px; text-align: center; font-size: 16px; color: var(--orange); }
  .vision .rule { left: 262px; top: 51px; width: 32px; height: 1.2px; background: var(--ink-soft); }
  .vision .copy { left: 208px; top: 64px; width: 144px; font-size: 5.5px; line-height: 1.4; text-align: justify; color: var(--ink); }
  .vision .copy p + p { margin-top: 6px; }

  /* Slide 8 — values */
  .values .photo { inset: 0; background: radial-gradient(ellipse at 50% 22%, #4f6f5e 0%, #7d9a89 22%, #eef0ee 48%, #f6f6f6 100%); }
  .values .title { left: 0; width: 368px; top: 78px; text-align: center; font-size: 17px; color: var(--orange); }
  .values .rule { left: 168px; top: 103px; width: 32px; height: 1.2px; background: var(--green); }
  .values ul { left: 0; width: 368px; top: 114px; list-style: none; text-align: center; font-size: 6.1px; line-height: 1.18; color: var(--ink); }
</style>
</head>
<body>

<!-- Cover -->
<section class="slide cover col-left row-1">
  <div class="photo" role="img" aria-label="Soft light photograph of a calm white interior with a framed shelf"></div>
  <div class="abs band"></div>
  <svg class="abs notch" width="26" height="14" viewBox="0 0 26 14"><polygon points="0,0 26,0 13,14" fill="var(--orange)"/></svg>
  <div class="abs name-plate">
    <span class="ring"></span>
    <span class="name">Korvel Mint</span>
  </div>
</section>

<!-- Activity intro -->
<section class="slide intro col-right row-1">
  <div class="photo" role="img" aria-label="Photograph of a glass skyscraper corner against a pale sky"></div>
  <h2 class="abs title">Activity &amp; Contest</h2>
  <div class="abs pitch"><em>Korvel Mint</em> is a management, organization and performance improvement consulting firm.</div>
  <div class="abs convictions">
    <h3>Our convictions:</h3>
    <p>In a hyper-competitive environment, only organizations able to quickly adapt will survive. Digital companies will have a competitive advantage because they will understand their ecosystem better, faster and will act more effectively than others.</p>
  </div>
  <div class="brand-mark"><span class="dot"></span>Korvel Mint</div>
</section>

<!-- Differences -->
<section class="slide differences col-left row-2">
  <svg class="abs panel" width="368" height="206" viewBox="0 0 368 206">
    <polygon points="0,0 227,0 227,160 214,173 227,186 227,206 0,206" fill="var(--green)"/>
  </svg>
  <h2 class="abs title">Activity &amp; Contest</h2>
  <h3 class="abs">Our differences :</h3>
  <ul class="abs points">
    <li><svg width="9" height="12" viewBox="0 0 9 12"><polyline points="1.5,1.5 7,6 1.5,10.5" fill="none" stroke="var(--orange)" stroke-width="2.4"/></svg><span>Use Lean and Agile known methods in innovative ways, creating quickly measurable value.</span></li>
    <li><svg width="9" height="12" viewBox="0 0 9 12"><polyline points="1.5,1.5 7,6 1.5,10.5" fill="none" stroke="var(--orange)" stroke-width="2.4"/></svg><span>Avoid stress and permanent emergency, accept mistakes to bounce back quickly.</span></li>
  </ul>
  <div class="photo" role="img" aria-label="Photograph of a person sketching a process diagram on a whiteboard"></div>
  <div class="abs mission">
    <h4>Our Mission</h4>
    <p>is to support the digital transformation of our clients.</p>
  </div>
  <div class="brand-mark"><span class="dot"></span>Korvel Mint</div>
</section>

<!-- Name explanation -->
<section class="slide naming col-right row-2">
  <h2 class="abs title">Name Explanation</h2>
  <div class="photo" role="img" aria-label="Photograph of a bright lounge with chairs, a plant and a patterned rug"></div>
  <div class="abs card-outline">
    <h4>Korvel</h4>
    <ul><li>• No stress</li><li>• Respect</li><li>• Human centric</li><li>• Accept mistakes</li></ul>
  </div>
  <div class="abs card-fill">
    <h4>Mint</h4>
    <ul><li>• Value for customers<br>&nbsp;&nbsp;and for ourselves</li><li>• Value by action</li><li>• Quick Value</li><li>• Measurable value</li></ul>
  </div>
  <div class="brand-mark"><span class="dot"></span>Korvel Mint</div>
</section>

<!-- Paradoxes -->
<section class="slide paradoxes col-left row-3">
  <div class="photo" role="img" aria-label="Faded photograph of a white desk with a notebook and laptop"></div>
  <div class="abs shade"></div>
  <h2 class="abs title">Paradoxes we defend</h2>
  <svg class="abs icons" width="368" height="206" viewBox="0 0 368 206">
    <g fill="var(--white)" fill-opacity="0.85" stroke="#7a7a7a" stroke-width="2.4">
      <circle cx="41" cy="88" r="16"/>
      <circle cx="97" cy="108" r="16"/>
      <circle cx="153" cy="86" r="16"/>
      <circle cx="212" cy="107" r="16" fill-opacity="0.25"/>
      <circle cx="269" cy="82" r="16" fill-opacity="0.25"/>
      <circle cx="326" cy="106" r="16" fill-opacity="0.25"/>
    </g>
    <g fill="none" stroke="var(--orange)" stroke-width="1.6" stroke-linecap="round" stroke-linejoin="round">
      <rect x="32" y="80" width="18" height="12" rx="1"/><line x1="41" y1="92" x2="41" y2="96"/><line x1="37" y1="96" x2="45" y2="96"/>
      <polygon points="100,97 91,110 97,110 94,119 104,105 98,105"/>
      <path d="M160 82 A8 8 0 1 0 161 91"/><polyline points="156,80 160,82 158,86"/>
      <rect x="202" y="102" width="20" height="9" transform="rotate(-35 212 107)"/>
      <path d="M260 88 A10 10 0 1 1 278 88"/><line x1="269" y1="84" x2="274" y2="78"/>
      <circle cx="321" cy="100" r="3"/><circle cx="331" cy="100" r="3"/><path d="M315 113 v-3 a5 5 0 0 1 11 0 M326 113 v-3 a5 5 0 0 1 11 0"/>
    </g>
  </svg>
  <span class="label" style="left:1px;top:114px;">Korvel and Digital</span>
  <span class="label" style="left:57px;top:134px;">Korvel and Quick</span>
  <span class="label" style="left:113px;top:112px;">Korvel and Action</span>
  <span class="label on-shade" style="left:186px;top:133px;width:60px;">Mint and Measurable</span>
  <span class="label on-shade" style="left:229px;top:112px;">Mint and Quick</span>
  <span class="label on-shade wrap" style="left:286px;top:133px;">Customers and Employees, both first</span>
  <div class="brand-mark"><span class="dot"></span>Korvel Mint</div>
</section>

<!-- Mission -->
<section class="slide mission-slide col-right row-3">
  <div class="photo" role="img" aria-label="Photograph of a wooden sideboard with small potted cacti against a grey wall with white triangles"></div>
  <h2 class="abs title">Mission</h2>
  <div class="abs rule"></div>
  <p class="abs">Support our customers in their digital transformation with agile and innovative approaches results oriented</p>
  <div class="brand-mark"><span class="dot"></span>Korvel Mint</div>
</section>

<!-- Vision -->
<section class="slide vision col-left row-4">
  <div class="photo" role="img" aria-label="Photograph of a bright staircase with metal railings"></div>
  <h2 class="abs title">Vision</h2>
  <div class="abs rule"></div>
  <div class="abs copy">
    <p>Organizational transformations are often made with top-down approaches which require significant lead times.</p>
    <p>The vagaries of time, complexity, context uncertainty make it almost impossible ROI measurement. Furthermore, backtracking are difficult and expensive.</p>
    <p>To address these weaknesses, we propose an innovative approach with short cycle, in which the results of each step of the transformation can be measured quickly and quantitatively. This approach also allows to adjust the direction progressively according to obtained results.</p>
  </div>
  <div class="brand-mark"><span class="dot"></span>Korvel Mint</div>
</section>

<!-- Values -->
<section class="slide values col-right row-4">
  <div class="photo" role="img" aria-label="Photograph of a spiky green succulent in a white pot"></div>
  <h2 class="abs title">Value</h2>
  <div class="abs rule"></div>
  <ul class="abs">
    <li>People centric</li><li>Honesty / Caring</li><li>Open mind</li><li>Anticipation</li><li>Customer focus</li><li>Well-being</li><li>Engagement</li><li>Pragmatism</li><li>Direct to the point</li><li>Little, quick &amp; perfect</li><li>Pride</li>
  </ul>
  <div class="brand-mark"><span class="dot"></span>Korvel Mint</div>
</section>

</body>
</html>
```